Flyer für ambulanten Pflegedienst
Zielgruppe
Ambulanter Pflegedienst in Gründung. Habe schon ein Logo und Text. Zielgruppe sind Pflege und Hilfsbedürftige Menschen

```html
<!DOCTYPE html>
<html lang="de">
<head>
<meta charset="utf-8">
<title>Pflege Hafen – Flyer</title>
<link href="https://fonts.googleapis.com/css2?family=Poppins:wght@400;500;600;700&display=swap" rel="stylesheet">
<style>
:root{
  --teal:#4bb8ad;
  --blue:#0a93b8;
  --blue-dark:#0b7a9c;
  --ink:#1f1f1f;
  --paper:#ffffff;
  --paper-shade:#f1f3f4;
  --stage:#e4e5e6;
}
*{box-sizing:border-box;margin:0;padding:0}
html,body{width:1200px;height:1117px;overflow:hidden}
body{background:var(--stage);font-family:'Poppins',sans-serif;color:var(--ink);position:relative}
.page{position:absolute;top:182px;width:530px;height:752px;background:linear-gradient(180deg,var(--paper) 0%,var(--paper-shade) 100%);overflow:hidden;box-shadow:0 4px 14px rgba(0,0,0,.18)}
.page--front{left:57px}
.page--back{left:612px}
.abs{position:absolute}
p,li{font-size:8.6px;line-height:10.8px}
ul{list-style:none}
ul li{position:relative;padding-left:9px}
ul li::before{content:"";position:absolute;left:1px;top:4px;width:3px;height:3px;border-radius:50%;background:currentColor}
.list--teal li::before{background:var(--teal)}

/* front */
.hero-photo{left:0;top:0;width:530px;height:190px;background:linear-gradient(120deg,#d8d4cf 0%,#eeeceb 40%,#c9cfd3 75%,#e9ecee 100%)}
.hero-cut{left:0;top:0;width:530px;height:190px}
.brand{left:170px;top:138px;width:200px;display:flex;align-items:center;gap:6px}
.brand__dot{width:22px;height:22px;border-radius:50%;background:var(--teal);flex:none}
.brand__name{font-size:21px;font-weight:600;color:var(--blue-dark);line-height:1}
.brand__sub{left:170px;top:164px;width:200px;text-align:center;font-size:6px;font-weight:600;color:var(--blue-dark);line-height:8px}
.intro{left:50px;top:201px;width:430px;text-align:center}
.intro p+p{margin-top:10.8px}
.service-box{left:30px;top:355px;width:469px;height:343px;border:2px solid var(--teal);border-radius:16px;background:rgba(255,255,255,.7);box-shadow:6px 6px 0 #e2e5e6}
.tab{height:17px;border-radius:3px;background:linear-gradient(90deg,var(--blue-dark),var(--blue));color:#fff;font-weight:700;font-size:11px;line-height:17px;text-align:center}
.col{position:absolute}
.col .tab{margin-bottom:8px}
.col p{margin-bottom:12px}
.care-basic{left:22px;top:15px;width:185px}
.care-medical{left:237px;top:15px;width:210px}
.care-24{left:20px;top:226px;width:426px}
.care-24 p{text-align:center;margin:6px 0 10px;}
.two-col{display:flex;gap:28px}
.two-col ul:first-child{width:245px}
.wave{left:0;bottom:0;width:530px;height:56px}

/* back */
.side-strip{left:0;top:0;width:11px;height:350px;background:var(--teal)}
.house-box{left:37px;top:0;width:215px;height:246px;background:linear-gradient(160deg,var(--blue) 0%,#1aa3c3 60%,var(--blue-dark) 100%);border-radius:0 0 18px 18px;color:#fff;padding:30px 18px 0 20px}
.house-box h2{font-size:11px;line-height:13px;font-weight:700;margin-bottom:6px}
.house-box p{margin-bottom:8px}
h3.head{font-size:11px;line-height:13px;font-weight:700;color:var(--blue)}
.relief{left:274px;top:30px;width:210px}
.relief h3{margin-bottom:4px}
.relief p{margin-bottom:8px}
.respite{left:56px;top:264px;width:200px}
.respite h3{margin-bottom:4px}
.inline-list{display:flex;gap:12px;margin-top:6px}
.everyday{left:274px;top:221px;width:215px}
.everyday h3{margin-bottom:3px}
.everyday p{margin-bottom:7px}
.everyday .two-col{gap:8px}
.everyday .two-col ul:first-child{width:103px}
.process-box{left:31px;top:379px;width:469px;height:311px;border:2px solid var(--teal);border-radius:16px;background:rgba(255,255,255,.75);box-shadow:6px 6px 0 #e2e5e6;padding:16px 22px 0 22px}
.process-box>p{margin-bottom:10.8px}
.process-grid{display:grid;grid-template-columns:1fr 1fr;column-gap:22px}
.process-grid h3{color:var(--teal);margin:5px 0 2px}
</style>
</head>
<body>

<section class="page page--front">
  <div class="abs hero-photo" role="img" aria-label="Foto: Pflegekraft mit Stift und Klemmbrett am Tisch, daneben eine Medikamentendose"></div>
  <svg class="abs hero-cut" viewBox="0 0 530 190" aria-hidden="true">
    <path d="M0,150 C110,168 150,110 265,110 C380,110 420,168 530,150 L530,190 L0,190Z" fill="#ffffff"/>
    <path d="M0,130 L105,178 L120,178 L0,140Z" fill="var(--teal)"/>
    <path d="M530,130 L425,178 L410,178 L530,140Z" fill="var(--teal)"/>
  </svg>
  <div class="abs brand"><span class="brand__dot"></span><span class="brand__name">Pflege Hafen</span></div>
  <div class="abs brand__sub">ambulanter Pflegedienst Lorenhof UG<br>Haftungsbeschränkt</div>

  <div class="abs intro">
    <p>Uns liegt es am Herzen durch qualitativ hochwertige und individuelle Unterstützungsleistungen den Menschen ein selbstbestimmtes Leben zu ermöglichen. Wir setzen auf Fachkompetenz und Empathie, um sicherzustellen, dass unsere Kunden die bestmögliche medizinische Versorgung erhalten.</p>
    <p>Unsere Dienstleistung umfasst die ambulante Pflege gemäß SGB XI sowie die Behandlungspflege gemäß SGB V. Betreuungs- und Entlastungszeiten nach § 45 SGB XI um Menschen im Alltag zu unterstützen und ihre Lebensqualität zu steigern.</p>
    <p>Pflegebedürftig ist, wer aufgrund einer körperlichen, geistigen oder seelischen Krankheit bzw. Behinderung in erheblichen Umfang Hilfe bis hin zur vollumfänglichen Betreuung benötigt. Die Leistungen des Altenpflege- und Seniorenbetreuungsdienstes erstrecken sich auf die <strong>Grundpflege, Behandlungspflege, 24-Stundenpflege,</strong></p>
  </div>

  <div class="abs service-box">
    <div class="col care-basic">
      <div class="tab">Grundpflege</div>
      <p>In der Grundpflege werden die Pflegepersonenin der Verrichtung alltäglicher Grundverrichtungen unterstützt, z.B.</p>
      <ul>
        <li>Duschen</li><li>Baden</li><li>Zahnpflege Kämmen</li><li>Rasieren</li><li>An- und Auskleiden</li><li>Hilfsmittelversorgung</li><li>Mobilisation</li><li>Prophylaxen</li><li>Nahrungsaufnahme</li><li>Toilettengang u.s.w.</li>
      </ul>
    </div>
    <div class="col care-medical">
      <div class="tab">Behandlungspflege</div>
      <p>Die Behandlungspflege umfasst alle Pflegedienste, die auf ärztlicher Verordnung hin vom Pflegepersonal durchgeführt werden, z. B.</p>
      <ul>
        <li>Pulsmessung</li><li>Blutdruckmessung</li><li>Blutzuckermessung</li><li>Wundversorgung</li><li>Verbandswechsel</li><li>Injektionen (z.b. Insulin)</li><li>Stellen der Medikamente</li><li>Anlegen von Kompressionsverbänden</li><li>An- und Ausziehen von<br>Kompressionsstrümpfen u.s.w.</li>
      </ul>
    </div>
    <div class="col care-24">
      <div class="tab">24-Stunden Pflege</div>
      <p>In verschiedenen Situationen ist die stundenweise Pflege nicht ausreichend, z.B. in der Folgezeit eines Krankenhausaufenthaltes. Es wird eine 24-Stunden-Pflege angeboten, im Rahmen derer das Pflegepersonal rund um die Uhr erreichbar ist. Typische Leistungen sind:</p>
      <div class="two-col">
        <ul><li>Überwachung der Vitalsituation des Patienten</li><li>Verabreichung von Medikamenten<br>Wundversorgung</li></ul>
        <ul><li>Verbandswechsel</li><li>Katheter Versorgung u.s.w.</li></ul>
      </div>
    </div>
  </div>

  <svg class="abs wave" viewBox="0 0 530 56" preserveAspectRatio="none" aria-hidden="true">
    <path d="M0,0 C150,30 380,30 530,0 L530,56 L0,56Z" fill="var(--teal)"/>
    <path d="M0,22 C170,52 360,38 530,16 L530,56 L0,56Z" fill="#ffffff"/>
    <path d="M0,26 C170,56 360,42 530,20 L530,56 L0,56Z" fill="var(--blue)"/>
  </svg>
</section>

<section class="page page--back">
  <div class="abs side-strip"></div>
  <div class="abs house-box">
    <h2>Hauswirtschaftliche<br>Versorgung</h2>
    <p>In der hauswirtschaftlichen Versorgung werden sämtliche hauswirtschaftlichen Tätigkeiten übernommen, z.B.</p>
    <ul>
      <li>Einkaufen</li><li>Besorgungen</li><li>Zubereitung von Mahlzeiten</li><li>AbwaschenWäsche waschen</li><li>Bügeln</li><li>Reinigungsarbeiten (Aufräumen, Toilette, Bad, Küche, Wohn- und Schlafbereich, Staubsaugen, Staubwischen)</li><li>Betreuung von Haustieren</li><li>Heizen der Wohnung (Holz, Kohle, Öl)</li><li>Fahrdienste</li>
    </ul>
  </div>

  <div class="abs relief">
    <h3 class="head">Betreuungs- und Entlastungsleistungen nach § 45 SGB XI</h3>
    <p>Voraussetzung ist das Vorliegen eines Pflegegrades. Bei der Antragstellung eines Pflegegrades sind wir behilflich und begleiten die Begutachtung durch den Medizinischen Dienst der Krankenkassen.</p>
    <ul class="list--teal" style="width:165px">
      <li>Unterstützung bei der Haushaltsführung</li><li>Einkaufen</li><li>Begleitung zu Ärzten</li><li>Arzttermine vereinbaren</li><li>Unterstützung beim Ausfüllen von Formularen und Anträgen</li><li>Spaziergänge</li>
    </ul>
  </div>

  <div class="abs respite">
    <h3 class="head">Verhinderungspflege</h3>
    <p>Das Angebot im Bereich Verhinderungspflege richtet sich an die Angehörigen, die bei der Pflege eine stundenweise Entlastung benötigen. Typische Anlässe sind z.B.</p>
    <ul class="inline-list list--teal"><li>Urlaub</li><li>Krankheit</li><li>Überlastung</li></ul>
  </div>

  <div class="abs everyday">
    <h3 class="head">Alltagsbegleitung</h3>
    <p>In der Alltagsbegleitung werden die Pflegepersonen in allen alltäglichen Tätigkeiten und Freizeitaktivitäten unterstützt und begleitet. Typische Leistungen sind z.B.</p>
    <div class="two-col">
      <ul class="list--teal"><li>Arztbesuche</li><li>Behördengänge</li><li>Kulturelle Veranstaltungen</li><li>Spaziergänge</li><li>Ausflüge</li></ul>
      <ul class="list--teal"><li>Wanderungen</li><li>Stadtbummel</li><li>Restaurantbesuche</li><li>Friseurbesuche</li><li>Gedächtnistraining u.s.w.</li></ul>
    </div>
  </div>

  <div class="abs process-box">
    <p>Der Altenpflege- und Seniorenbetreuungsdienst führt sämtliche Pflegeleistungen kompetent, professionell und zuverlässig aus. Das oberste Ziel der Pflege ist die Sicherung und Verbesserung der Lebensqualität und das Bewahren des gewohnten Lebensumfelds der Pflegepersonen. Krankenhaus- und Betreuungsheimaufenthalte sollen möglichst vermieden werden. Diesem Grundgedanken liegt die Erkenntnis zu Grunde, dass in einer vertrauten Umgebung Kranke oft schneller gesünder werden und gerade ältere Menschen sich zu. Hause besonders wohl und geborgen fühlen.</p>
    <p>Der grundlegende Geschäftsprozess des Unternehmens gliedert sich in die Bereiche Beratung, Pflegekonzept, Vertragsabschluss und Pflege:</p>
    <div class="process-grid">
      <div>
        <h3 class="head">Beratung</h3>
        <p>Kunden werden ausführlich unter Berücksichtigung ihrer Wünsche und Vorstellungen beraten. Denn das vorhandene Pflegeangebot bietet eine Vielzahl an Möglichkeiten. Wichtig ist der Aufbau von Vertrauen.</p>
        <h3 class="head" style="margin-top:8px">Pflegekonzept</h3>
        <p>Unter Berücksichtigung aller Möglichkeiten und Patientenwünsche wird ein individuelles Leistungskonzept entwickelt und eine verbindliche Kostenaufstellung erstellt.</p>
      </div>
      <div>
        <h3 class="head">Vertragsschluss</h3>
        <p>Alle Aufträge mit Kunden werden in schriftlicher Form geschlossen und beidseitig unterzeichnet.</p>
        <h3 class="head" style="margin-top:8px">Pflege</h3>
        <p>Die vereinbarten Pflegeleistungen werden nun umgesetzt. Dabei kann der Kunde stets eine hohe Ausführungsqualität erwarten. Es wird für jeden Kunden eine Mappe zur Pflegedokumentation geführt (Pflegesoftware, die stets vom Kunden sowie seinen Angehörigen eingesehen werden kann).</p>
      </div>
    </div>
  </div>

  <svg class="abs wave" viewBox="0 0 530 56" preserveAspectRatio="none" aria-hidden="true">
    <path d="M0,0 C150,30 380,30 530,0 L530,56 L0,56Z" fill="var(--teal)"/>
    <path d="M0,22 C170,52 360,38 530,16 L530,56 L0,56Z" fill="#ffffff"/>
    <path d="M0,26 C170,56 360,42 530,20 L530,56 L0,56Z" fill="var(--blue)"/>
  </svg>
</section>

</body>
</html>
```